Small business updating business cards

We have already updated our logo via Pixel Forum and downloaded it (hopefully) for you to use. Now an updated set of business cards for Neil Pollard and Stuart Pollard are also needed... we are also hoping that a copy of our outdated business card designs have uploaded successfully as Microsoft Publisher files. Our Strength Through Unity motto has died a slow death so we are hoping to remove it (and other superfluous lingo if the graphic covers the idea) and instead opt for a fancy graphic (?) on the second side of the card that really reflects our desire to obtain product / haulage from Road Transport / Yard Operators and convert legs of their haulage to rail freight where profitable (bulk haulage / containterised etc). Can you help us look larger, bolder and more robust than we really are (two man show)?
Target Market(s)
Transport Industry
Industry/Entity Type
Business
Contact Information for Business Card
Card details for both N Pollard and S Pollard have been uploaded on the publisher files
Colors
Designer to choose colors to be used in the design.
Requirements
Must have
- Similar theme both sides of card
Should not have
- Black on one side white on the other

```html
<!DOCTYPE html>
<html lang="en">
<head>
<meta charset="utf-8">
<title>Railmark Business Cards</title>
<link href="https://fonts.googleapis.com/css2?family=Roboto:wght@400;500;700&family=Exo+2:wght@700&display=swap" rel="stylesheet">
<style>
  :root {
    --page: #e4e4e4;
    --card-white: #f7f7f7;
    --teal: #2386a6;
    --teal-top: #2a87a3;
    --olive-bottom: #918b4b;
    --gold: #d7aa3a;
    --ink: #2f2f2f;
    --ink-soft: #4a4a4a;
    --white-soft: rgba(255,255,255,0.85);
  }
  * { margin: 0; padding: 0; box-sizing: border-box; }
  html, body {
    width: 1200px; height: 576px; overflow: hidden;
    background: var(--page);
    font-family: "Roboto", Arial, sans-serif;
  }
  .canvas { position: relative; width: 1200px; height: 576px; }
  .card {
    position: absolute; border-radius: 12px; overflow: hidden;
    box-shadow: 0 3px 6px rgba(0,0,0,0.25);
  }

  /* Back side */
  .card--back {
    left: 82px; top: 139px; width: 484px; height: 293px;
    background: linear-gradient(to bottom, var(--teal-top), var(--olive-bottom));
    color: #fff; text-align: center;
  }
  .back-name {
    position: absolute; left: 0; right: 0; top: 78px;
    font-weight: 700; font-size: 58px; line-height: 68px;
    letter-spacing: -0.5px; color: #fff;
  }
  .freight-graphic {
    position: absolute; left: 70px; right: 70px; top: 166px; height: 52px;
    border-radius: 6px;
    background: linear-gradient(to right,
      rgba(215,170,58,0.35), rgba(255,255,255,0.18) 50%, rgba(35,134,166,0.4));
  }
  .back-contact {
    position: absolute; left: 0; right: 0; top: 234px;
    font-size: 13px; line-height: 19px; color: var(--white-soft);
  }

  /* Front side */
  .card--front {
    left: 602px; top: 138px; width: 481px; height: 292px;
    background: var(--card-white);
  }
  .edge-tab {
    position: absolute; right: -14px; top: 34px;
    width: 30px; height: 64px; border-radius: 50%;
    background: var(--teal);
  }
  .brand-name {
    position: absolute; left: 20px; top: 34px;
    font-weight: 700; font-size: 44px; line-height: 52px;
    letter-spacing: -0.5px; color: var(--teal);
  }
  .person-name {
    position: absolute; left: 20px; top: 134px;
    font-family: "Exo 2", "Roboto", sans-serif; font-weight: 700;
    font-size: 21px; line-height: 26px; color: var(--teal);
  }
  .person-role {
    position: absolute; left: 20px; top: 162px;
    font-size: 10px; line-height: 12px; color: var(--ink);
  }
  .rule {
    position: absolute; left: 110px; right: 21px; top: 169px; height: 1.5px;
    background: linear-gradient(to right, var(--gold), var(--teal));
  }
  .address {
    position: absolute; left: 20px; top: 196px; font-style: normal;
    font-size: 13.5px; line-height: 19px; color: var(--ink-soft);
  }
  .contact-list {
    position: absolute; left: 20px; top: 238px; list-style: none;
    font-size: 13.5px; line-height: 19px; color: var(--ink-soft);
  }
  .contact-list li { display: flex; align-items: center; gap: 10px; }
  .contact-list svg { width: 14px; height: 12px; fill: var(--teal); }
  .services {
    position: absolute; right: 21px; top: 196px; list-style: none;
    text-align: right; font-size: 13.5px; line-height: 19px; color: var(--ink-soft);
  }
  .services li::after { content: " \00AB"; }
  .services li.last::after { content: "\00A0\00A0\00A0"; }
  .web {
    position: absolute; right: 21px; top: 256px;
    font-size: 13.5px; line-height: 19px; color: var(--ink-soft);
  }
  .web span { color: var(--teal); }
</style>
</head>
<body>
<main class="canvas">
  <section class="card card--back" aria-label="Card back">
    <div class="back-name">Railmark</div>
    <div class="freight-graphic" role="img" aria-label="Graphic of road haulage trucks handing containers and bulk loads over to a rail freight train"></div>
    <div class="back-contact">
      <div>www.railmark.com.au</div>
      <div>office@railmark.com.au &nbsp;|&nbsp; bookings@railmark.com.au</div>
    </div>
  </section>

  <section class="card card--front" aria-label="Card front">
    <div class="edge-tab"></div>
    <div class="brand-name">Railmark</div>
    <div class="person-name">Neil Pollard</div>
    <div class="person-role">Managing Director</div>
    <div class="rule"></div>
    <address class="address">
      14 Corvin Street<br>Kelsey Park NSW 2290
    </address>
    <ul class="contact-list">
      <li>
        <svg viewBox="0 0 14 12" aria-hidden="true"><path d="M1 3 Q7 -1 13 3 L11 5 L9 3.5 L5 3.5 L3 5 Z M3 6 L11 6 L12 11 L2 11 Z"/></svg>
        0400 128 733
      </li>
      <li>
        <svg viewBox="0 0 14 12" aria-hidden="true"><path d="M1 2 L13 2 L13 10 L1 10 Z M1.5 2.5 L7 7 L12.5 2.5" stroke="#fff" stroke-width="1"/></svg>
        pollardn@railmark.com.au
      </li>
    </ul>
    <ul class="services">
      <li>Strategic Alliance Partners</li>
      <li>Providing Logistical</li>
      <li class="last">Freight Solutions</li>
    </ul>
    <div class="web">www.<span>railmark</span>.com.au</div>
  </section>
</main>
</body>
</html>
```